IT Company based on Biology Business Needs a Business Card Design

We need a business card design for a new company called 'Lumen CELL'. We develop the machine learning solutions especially focused on deep learning algorithms for biology industry. Our initial product is a vision detection on biological images to help doctors diagnose the symptoms. We would like to see designs that use the color green.

Industry/Entity Type

Business

```html
<!DOCTYPE html>
<html lang="en">
<head>
<meta charset="utf-8">
<title>Lumen CELL – Business Card</title>
<link rel="stylesheet" href="https://fonts.googleapis.com/css2?family=Arimo:wght@400;700&display=swap">
<style>
  :root {
    --stage: #d9d6d2;
    --card: #1c1c1c;
    --card-edge: #262626;
    --green: #5cc43a;
    --green-deep: #3fa52e;
    --ink-light: #f2f2f2;
    --emboss: #3a3a3a;
    --divider: #9a9a9a;
  }
  * { box-sizing: border-box; margin: 0; padding: 0; }
  html, body {
    width: 1200px;
    height: 787px;
    overflow: hidden;
    background: var(--stage);
    font-family: "Arimo", Arial, sans-serif;
  }
  .stage {
    width: 1200px;
    height: 787px;
    display: flex;
    align-items: center;
    justify-content: center;
    gap: 40px;
  }
  .card {
    width: 540px;
    height: 309px;
    background: var(--card);
    border: 1px solid var(--card-edge);
    box-shadow: 0 10px 24px rgba(0,0,0,0.25);
    position: relative;
  }
  .card-front {
    display: flex;
    align-items: center;
    justify-content: center;
  }
  .wordmark {
    display: flex;
    align-items: center;
    gap: 12px;
    font-weight: 700;
    letter-spacing: 0.5px;
    white-space: nowrap;
  }
  .wordmark-dot {
    width: 16px;
    height: 16px;
    border-radius: 50%;
  }
  .card-front .wordmark { font-size: 46px; color: var(--emboss); }
  .card-front .wordmark-dot { background: var(--emboss); }

  .card-back .wordmark {
    position: absolute;
    left: 34px;
    top: 128px;
    font-size: 34px;
    color: var(--green);
  }
  .card-back .wordmark-dot { width: 12px; height: 12px; background: var(--green); }
  .divider {
    position: absolute;
    left: 290px;
    top: 56px;
    width: 1px;
    height: 200px;
    background: linear-gradient(to bottom, transparent, var(--divider) 25%, var(--divider) 75%, transparent);
  }
  .contact {
    position: absolute;
    left: 314px;
    top: 62px;
    color: var(--ink-light);
    font-size: 14.5px;
    line-height: 1.3;
  }
  .contact-name { color: var(--green); font-weight: 700; font-size: 19px; }
  .contact-title { color: var(--green-deep); font-size: 13px; margin-bottom: 14px; }
  .contact-address { margin-bottom: 12px; }
  .contact-list { list-style: none; }
  .contact-list li { display: flex; align-items: center; gap: 8px; height: 20px; }
  .contact-icon { width: 13px; height: 13px; fill: var(--green); flex: none; }
</style>
</head>
<body>
<main class="stage">
  <section class="card card-front" aria-label="Card front">
    <div class="wordmark"><span class="wordmark-dot"></span>LUMEN CELL</div>
  </section>

  <section class="card card-back" aria-label="Card back">
    <div class="wordmark"><span class="wordmark-dot"></span>LUMEN CELL</div>
    <div class="divider"></div>
    <div class="contact">
      <p class="contact-name">Mara Lind</p>
      <p class="contact-title">President</p>
      <p class="contact-address">1270 Harbor Lane<br>Fairview, NY 11020</p>
      <ul class="contact-list">
        <li>
          <svg class="contact-icon" viewBox="0 0 16 16" aria-hidden="true"><path d="M3 1h3l1.5 4-2 1.3a9 9 0 0 0 4.2 4.2L11 8.5l4 1.5v3a2 2 0 0 1-2 2A12 12 0 0 1 1 3a2 2 0 0 1 2-2z"/></svg>
          555 0142 7781
        </li>
        <li>
          <svg class="contact-icon" viewBox="0 0 16 16" aria-hidden="true"><path d="M4.5 0h7A1.5 1.5 0 0 1 13 1.5v13a1.5 1.5 0 0 1-1.5 1.5h-7A1.5 1.5 0 0 1 3 14.5v-13A1.5 1.5 0 0 1 4.5 0zM5 2v10h6V2zm3 11a1 1 0 1 0 0 2 1 1 0 0 0 0-2z"/></svg>
          555 0199 3360
        </li>
        <li>
          <svg class="contact-icon" viewBox="0 0 16 16" aria-hidden="true"><path d="M0 3h16v1.2L8 9 0 4.2zM0 5.8 8 10.6l8-4.8V13H0z"/></svg>
          mara@lumencell.com
        </li>
        <li>
          <svg class="contact-icon" viewBox="0 0 16 16" aria-hidden="true"><path d="M8 0a8 8 0 1 0 0 16A8 8 0 0 0 8 0zm0 1.5c.9 0 1.9 1.9 2.2 5.3H5.8C6.1 3.4 7.1 1.5 8 1.5zM5.8 8.2h4.4C9.9 11.6 8.9 14.5 8 14.5s-1.9-2.9-2.2-6.3zM1.6 6.8a6.5 6.5 0 0 1 3.1-4.4 11 11 0 0 0-.4 4.4zm0 1.4h2.7a11 11 0 0 0 .4 4.4 6.5 6.5 0 0 1-3.1-4.4zm12.8 0a6.5 6.5 0 0 1-3.1 4.4 11 11 0 0 0 .4-4.4zm0-1.4h-2.7a11 11 0 0 0-.4-4.4 6.5 6.5 0 0 1 3.1 4.4z"/></svg>
          www.lumencell.com
        </li>
      </ul>
    </div>
  </section>
</main>
</body>
</html>
```